Social Event Calendar for real estate ad

I need a one page - 8 1/2 x 11 card (front and back) designed to include a list of events and images. The design should look somewhat tropical and friendly utilizing the color Aqua Blue. I am a real estate broker in West Palm Beach, Florida.

Target Market(s)

Adult homeowners age 30-80 of Florida homes primarily in the West Palm Beach, Florida historic homes market. The purpose of the marketing piece is to provide interesting content on the social events occurring within the next 6 months in the area. The ad should portray the sender as an expert in the neighborhood. The call to action will be for the reader to contact the sender of the ad to determine the value of the reader's home.

Industry/Entity Type

Real Estate

Font styles to use
Other font styles liked:
• Helvetica

Colors
0092cd
00a990
e567a6

Requirements
Must have
• Must have a calendar listing of events similar to the screenshot provided but fitting 10 events for January and 10 for February.

```html
<!DOCTYPE html>
<html lang="en">
<head>
<meta charset="utf-8">
<title>Social Event Calendar</title>
<link rel="stylesheet" href="https://fonts.googleapis.com/css2?family=Roboto+Condensed:wght@300;400&display=swap">
<style>
  :root {
    --aqua-blue: #0092cd;
    --sea-green: #00a990;
    --paper: #ffffff;
    --photo-sky: #2f6fb5;
    --photo-shade: #1a2730;
  }
  * { margin: 0; padding: 0; box-sizing: border-box; }
  html, body { width: 927px; height: 1200px; overflow: hidden; }
  body {
    background: var(--aqua-blue);
    font-family: "Roboto Condensed", "Helvetica Neue", Helvetica, Arial, sans-serif;
    position: relative;
  }
  .calendar-card {
    position: absolute;
    left: 55px; top: 55px;
    width: 819px; height: 1089px;
    background: var(--paper);
    border-radius: 27px;
  }
  .month {
    position: absolute;
    left: 32px;
    width: 753px;
  }
  .month--january { top: 33px; }
  .month--february { top: 579px; }
  .month-header {
    position: relative;
    height: 47px;
  }
  .month-tab {
    width: 376px; height: 47px;
    background: var(--sea-green);
    border-top-left-radius: 12px;
    color: var(--paper);
    font-weight: 300;
    font-size: 30px;
    line-height: 47px;
    padding-left: 26px;
  }
  .month-rule {
    position: absolute;
    left: 376px; right: 0; bottom: 0;
    height: 4px;
    background: var(--sea-green);
  }
  .event-grid {
    display: grid;
    grid-template-columns: 377px 376px;
    grid-auto-rows: 72px;
    row-gap: 12.7px;
    margin-top: 21px;
    grid-auto-flow: column;
    grid-template-rows: repeat(5, 72px);
  }
  .event {
    display: flex;
    gap: 8px;
  }
  .event-photo {
    flex: 0 0 151px;
    height: 72px;
    background: linear-gradient(160deg, var(--photo-sky) 0%, #4b86c6 35%, #56636d 65%, var(--photo-shade) 100%);
  }
  .event-text {
    color: var(--aqua-blue);
    font-weight: 300;
    padding-top: 0;
  }
  .event-date { font-size: 12px; line-height: 15px; display: block; }
  .event-series, .event-name { font-size: 17.5px; line-height: 20.5px; display: block; text-transform: uppercase; }
  .event-location { font-size: 12px; line-height: 16px; display: block; }
</style>
</head>
<body>
<main class="calendar-card">

  <section class="month month--january">
    <header class="month-header">
      <h2 class="month-tab">January</h2>
      <div class="month-rule"></div>
    </header>
    <div class="event-grid">
      <article class="event"><div class="event-photo" role="img" aria-label="Palm trees in front of a white building under a blue sky"></div><div class="event-text"><span class="event-date">Sunday, 5th January 2014</span><span class="event-series">My Events</span><span class="event-name">Events Name Goes Here</span><span class="event-location">Location Name</span></div></article>
      <article class="event"><div class="event-photo" role="img" aria-label="Palm trees in front of a white building under a blue sky"></div><div class="event-text"><span class="event-date">Sunday, 5th January 2014</span><span class="event-series">My Events</span><span class="event-name">Events Name Goes Here</span><span class="event-location">Location Name</span></div></article>
      <article class="event"><div class="event-photo" role="img" aria-label="Palm trees in front of a white building under a blue sky"></div><div class="event-text"><span class="event-date">Sunday, 5th January 2014</span><span class="event-series">My Events</span><span class="event-name">Events Name Goes Here</span><span class="event-location">Location Name</span></div></article>
      <article class="event"><div class="event-photo" role="img" aria-label="Palm trees in front of a white building under a blue sky"></div><div class="event-text"><span class="event-date">Sunday, 5th January 2014</span><span class="event-series">My Events</span><span class="event-name">Events Name Goes Here</span><span class="event-location">Location Name</span></div></article>
      <article class="event"><div class="event-photo" role="img" aria-label="Palm trees in front of a white building under a blue sky"></div><div class="event-text"><span class="event-date">Sunday, 5th January 2014</span><span class="event-series">My Events</span><span class="event-name">Events Name Goes Here</span><span class="event-location">Location Name</span></div></article>
      <article class="event"><div class="event-photo" role="img" aria-label="Palm trees in front of a white building under a blue sky"></div><div class="event-text"><span class="event-date">Sunday, 5th January 2014</span><span class="event-series">My Events</span><span class="event-name">Events Name Goes Here</span><span class="event-location">Location Name</span></div></article>
      <article class="event"><div class="event-photo" role="img" aria-label="Palm trees in front of a white building under a blue sky"></div><div class="event-text"><span class="event-date">Sunday, 5th January 2014</span><span class="event-series">My Events</span><span class="event-name">Events Name Goes Here</span><span class="event-location">Location Name</span></div></article>
      <article class="event"><div class="event-photo" role="img" aria-label="Palm trees in front of a white building under a blue sky"></div><div class="event-text"><span class="event-date">Sunday, 5th January 2014</span><span class="event-series">My Events</span><span class="event-name">Events Name Goes Here</span><span class="event-location">Location Name</span></div></article>
      <article class="event"><div class="event-photo" role="img" aria-label="Palm trees in front of a white building under a blue sky"></div><div class="event-text"><span class="event-date">Sunday, 5th January 2014</span><span class="event-series">My Events</span><span class="event-name">Events Name Goes Here</span><span class="event-location">Location Name</span></div></article>
      <article class="event"><div class="event-photo" role="img" aria-label="Palm trees in front of a white building under a blue sky"></div><div class="event-text"><span class="event-date">Sunday, 5th January 2014</span><span class="event-series">My Events</span><span class="event-name">Events Name Goes Here</span><span class="event-location">Location Name</span></div></article>
    </div>
  </section>

  <section class="month month--february">
    <header class="month-header">
      <h2 class="month-tab">February</h2>
      <div class="month-rule"></div>
    </header>
    <div class="event-grid">
      <article class="event"><div class="event-photo" role="img" aria-label="Palm trees in front of a white building under a blue sky"></div><div class="event-text"><span class="event-date">Sunday, 2nd February 2014</span><span class="event-series">My Events</span><span class="event-name">Events Name Goes Here</span><span class="event-location">Location Name</span></div></article>
      <article class="event"><div class="event-photo" role="img" aria-label="Palm trees in front of a white building under a blue sky"></div><div class="event-text"><span class="event-date">Sunday, 2nd February 2014</span><span class="event-series">My Events</span><span class="event-name">Events Name Goes Here</span><span class="event-location">Location Name</span></div></article>
      <article class="event"><div class="event-photo" role="img" aria-label="Palm trees in front of a white building under a blue sky"></div><div class="event-text"><span class="event-date">Sunday, 2nd February 2014</span><span class="event-series">My Events</span><span class="event-name">Events Name Goes Here</span><span class="event-location">Location Name</span></div></article>
      <article class="event"><div class="event-photo" role="img" aria-label="Palm trees in front of a white building under a blue sky"></div><div class="event-text"><span class="event-date">Sunday, 2nd February 2014</span><span class="event-series">My Events</span><span class="event-name">Events Name Goes Here</span><span class="event-location">Location Name</span></div></article>
      <article class="event"><div class="event-photo" role="img" aria-label="Palm trees in front of a white building under a blue sky"></div><div class="event-text"><span class="event-date">Sunday, 2nd February 2014</span><span class="event-series">My Events</span><span class="event-name">Events Name Goes Here</span><span class="event-location">Location Name</span></div></article>
      <article class="event"><div class="event-photo" role="img" aria-label="Palm trees in front of a white building under a blue sky"></div><div class="event-text"><span class="event-date">Sunday, 2nd February 2014</span><span class="event-series">My Events</span><span class="event-name">Events Name Goes Here</span><span class="event-location">Location Name</span></div></article>
      <article class="event"><div class="event-photo" role="img" aria-label="Palm trees in front of a white building under a blue sky"></div><div class="event-text"><span class="event-date">Sunday, 2nd February 2014</span><span class="event-series">My Events</span><span class="event-name">Events Name Goes Here</span><span class="event-location">Location Name</span></div></article>
      <article class="event"><div class="event-photo" role="img" aria-label="Palm trees in front of a white building under a blue sky"></div><div class="event-text"><span class="event-date">Sunday, 2nd February 2014</span><span class="event-series">My Events</span><span class="event-name">Events Name Goes Here</span><span class="event-location">Location Name</span></div></article>
      <article class="event"><div class="event-photo" role="img" aria-label="Palm trees in front of a white building under a blue sky"></div><div class="event-text"><span class="event-date">Sunday, 2nd February 2014</span><span class="event-series">My Events</span><span class="event-name">Events Name Goes Here</span><span class="event-location">Location Name</span></div></article>
      <article class="event"><div class="event-photo" role="img" aria-label="Palm trees in front of a white building under a blue sky"></div><div class="event-text"><span class="event-date">Sunday, 2nd February 2014</span><span class="event-series">My Events</span><span class="event-name">Events Name Goes Here</span><span class="event-location">Location Name</span></div></article>
    </div>
  </section>

</main>
</body>
</html>
```